business card for WRT pty ltd

We require a business card that stands out . I have included our company flyer and would like the services listed to be put on the card so when we Give out the cards to customers they have an idea of services we provide. need the winning design to be in editable photo shop format, editable iMac pages format or editable windows publisher format, so that I can enter in names, email addresses, phone numbers etc myself. I have included a pdf documents of info / items needed on the card to use as reference please.
Updates

need more submissions

Need extra days to review

Sick

Target Market(s)

new customers

Contact Information for Business Card

details are on attached business card requirements file

Requirements
Must have
• I have attached a list of must haves

```html
<!DOCTYPE html>
<html lang="en">
<head>
<meta charset="utf-8">
<title>WRT pty ltd — Business Card</title>
<link rel="stylesheet" href="https://fonts.googleapis.com/css2?family=Montserrat:wght@700;800&family=Open+Sans:wght@400;600&display=swap">
<style>
  :root{
    --backdrop:#3a3f46;
    --card-black:#0b0b0c;
    --card-charcoal:#2a2b2e;
    --card-white:#f6f6f6;
    --ink:#1b1b1b;
    --ink-soft:#3c3c3c;
    --silver:#c9ccd1;
    --edge:#9a9da2;
    --orange:#f07a22;
    --list-text:#f2f2f2;
    --photo-sand:#b98456;
    --photo-sky:#a9c2cf;
  }
  *{box-sizing:border-box;margin:0;padding:0}
  html,body{width:1200px;height:900px;overflow:hidden}
  body{background:var(--backdrop);font-family:"Open Sans",Arial,sans-serif;position:relative}

  .card{position:absolute;left:250px;width:700px;height:400px;border-radius:26px;overflow:hidden;box-shadow:0 14px 30px rgba(0,0,0,.45)}
  .card--contact{top:30px;background:var(--card-white)}
  .card--services{top:470px;background:var(--card-black)}

  .brand-name{position:absolute;font-family:"Montserrat",Arial,sans-serif;font-weight:800;color:var(--silver);letter-spacing:6px;line-height:1}

  /* contact side */
  .contact__dark{position:absolute;inset:0;background:radial-gradient(circle at 75% 40%,var(--card-charcoal),var(--card-black) 70%);clip-path:polygon(66% 0,100% 0,100% 100%,54% 100%)}
  .contact__edge{position:absolute;inset:0;background:var(--edge);clip-path:polygon(65% 0,66% 0,54% 100%,53% 100%)}
  .card--contact .brand-name{right:40px;top:150px;font-size:84px}

  .person{position:absolute;left:28px;top:112px;text-align:right;width:172px}
  .person__name{font-family:"Montserrat",Arial,sans-serif;font-weight:800;font-size:20px;color:var(--ink);letter-spacing:.5px;white-space:nowrap}
  .person__title{font-size:14px;color:var(--ink-soft)}
  .divider{position:absolute;left:212px;top:102px;width:2px;height:84px;background:var(--ink)}
  .contacts{position:absolute;left:226px;top:100px;list-style:none;font-size:13px;color:var(--ink);line-height:1.75;white-space:nowrap}
  .contacts li{display:flex;align-items:center;gap:7px}
  .contacts svg{width:11px;height:11px;fill:var(--ink)}
  .address{position:absolute;left:42px;top:230px;font-size:14px;color:var(--ink-soft)}

  /* services side */
  .photo{position:absolute;inset:0;background:linear-gradient(160deg,var(--photo-sky) 0%,#8a8c86 30%,var(--photo-sand) 60%,#7a5434 100%);clip-path:polygon(0 0,52% 0,30% 100%,0 100%)}
  .services{position:absolute;inset:0;background:var(--card-black);clip-path:polygon(0 46%,44% 30%,36% 100%,0 100%)}
  .services__tab{position:absolute;left:160px;top:122px;background:var(--orange);color:#fff;font-weight:600;font-size:14px;padding:2px 12px;transform:rotate(-12deg);transform-origin:left bottom}
  .services__list{position:absolute;left:26px;top:200px;list-style:none;font-size:10.5px;color:var(--list-text);line-height:1.35;white-space:nowrap}
  .services__list li::before{content:"";display:inline-block;width:5px;height:5px;border-radius:50%;background:var(--orange);margin-right:7px;vertical-align:middle}
  .card--services .brand-name{right:70px;top:160px;font-size:84px}
</style>
</head>
<body>
  <section class="card card--contact" aria-label="Contact side">
    <div class="contact__dark"></div>
    <div class="contact__edge"></div>
    <div class="brand-name">WRT</div>
    <div class="person">
      <p class="person__name">DANIEL BROOK</p>
      <p class="person__title">Director</p>
    </div>
    <div class="divider"></div>
    <ul class="contacts">
      <li><svg viewBox="0 0 24 24"><path d="M6.6 10.8a15 15 0 0 0 6.6 6.6l2.2-2.2a1 1 0 0 1 1-.2 11 11 0 0 0 3.6.6 1 1 0 0 1 1 1V20a1 1 0 0 1-1 1A17 17 0 0 1 3 4a1 1 0 0 1 1-1h3.5a1 1 0 0 1 1 1 11 11 0 0 0 .6 3.6 1 1 0 0 1-.3 1z"/></svg>000 555 000</li>
      <li><svg viewBox="0 0 24 24"><path d="M2 5h20v14H2zm2 2v.5l8 5 8-5V7z"/></svg>email@wrtservices.com.au</li>
      <li><svg viewBox="0 0 24 24"><circle cx="12" cy="12" r="10"/></svg>www.wrtcentre.com</li>
    </ul>
    <p class="address">Lot 12 sample road Australia</p>
  </section>

  <section class="card card--services" aria-label="Services side">
    <div class="photo" role="img" aria-label="Photo of road train trucks and heavy machinery on red dirt"></div>
    <div class="services"></div>
    <span class="services__tab">Our Services</span>
    <ul class="services__list">
      <li>Over size loads/Hot Shot Loads</li>
      <li>Heavy Vehicle Recovery Services</li>
      <li>Portable Water Deliveries</li>
      <li>Road building/Maintenance</li>
      <li>Earthworks</li>
      <li>Sand &amp; Metal Supply &amp; Cartage</li>
      <li>Road Train Tippers</li>
      <li>Road Train Tankers</li>
      <li>Road Train Triple Tipper</li>
      <li>Drop Deck Trailers</li>
      <li>Mine Site accredited</li>
      <li>Equipment &amp; Operator</li>
    </ul>
    <div class="brand-name">WRT</div>
  </section>
</body>
</html>
```